Dravetti Business Cards

We need a business card design for Dravetti Mining.

This is a B2B company that buys and sells large machinery tires within the coal mining industry. The design should the strong, crisp and masculine. I have uploaded the company logo and rough mock-up of what the back of the card should look like. the front of the card should have the same look/feel as the back. I need editable templates for both the front and the back of the card.

Color scheme should be grey/green/black

Contact information to include on the card:
Name: Owen Pellsworth
Title: Managing Director
Phone: 972-555-0143
Address: 3157 Brantley #5 Dallas, TX 75209
Email: Owen@Dravetti-example.com

I am also opening a contest for letterhead design. If you submit a business card design, please also submit a letterhead design with the same look/feel. The winner of the business card design will also will the letter head and be paid for both.

Target Market(s)

Procurement men/women in the coal mining industry

Industry/Entity Type

Coal Mining

```html
<!DOCTYPE html>
<html lang="en">
<head>
<meta charset="utf-8">
<title>Dravetti Business Cards</title>
<link rel="stylesheet" href="https://fonts.googleapis.com/css2?family=Questrial&display=swap">
<style>
  :root {
    --backdrop: #3a5a5c;
    --card-black: #0b0b0b;
    --card-edge: #1c1c1c;
    --brand-green: #7ee021;
    --ink-white: #ffffff;
    --ink-black: #000000;
    --mark-grey: #a9adae;
  }
  * { margin: 0; padding: 0; box-sizing: border-box; }
  html, body {
    width: 1200px;
    height: 900px;
    overflow: hidden;
    background: var(--backdrop);
    font-family: "Questrial", sans-serif;
  }
  .canvas {
    position: relative;
    width: 1200px;
    height: 900px;
  }
  .card {
    position: absolute;
    left: 320px;
    width: 560px;
    height: 320px;
    background: var(--card-black);
    border: 1px solid var(--card-edge);
    box-shadow: 0 12px 30px rgba(0, 0, 0, 0.35);
    overflow: hidden;
  }
  .card--back { top: 100px; }
  .card--front { top: 470px; }

  .brand {
    position: absolute;
    display: flex;
    align-items: center;
    gap: 14px;
  }
  .brand__mark {
    width: 50px;
    height: 50px;
    border-radius: 50%;
    background: var(--mark-grey);
    flex: none;
  }
  .brand__name {
    color: var(--ink-white);
    font-size: 32px;
    letter-spacing: 1px;
    text-transform: uppercase;
    line-height: 1;
    white-space: nowrap;
  }
  .card--back .brand {
    left: 50%;
    top: 50%;
    transform: translate(-50%, -50%);
  }

  .front__haze {
    position: absolute;
    inset: 0;
    background:
      radial-gradient(circle 150px at 160px 140px, rgba(255,255,255,0.40) 0%, rgba(255,255,255,0.10) 40%, rgba(255,255,255,0) 100%),
      radial-gradient(circle 190px at 70px 270px, rgba(255,255,255,0.16) 0%, rgba(255,255,255,0.05) 55%, rgba(255,255,255,0) 100%);
  }
  .card--front .brand {
    left: 135px;
    top: 115px;
  }
  .card--front .brand__name { font-size: 30px; }

  .holder {
    position: absolute;
    right: 20px;
    top: 18px;
    text-align: right;
  }
  .holder__name {
    color: var(--ink-white);
    font-size: 18px;
    text-transform: uppercase;
    letter-spacing: 0.5px;
    line-height: 1.1;
  }
  .holder__name-initial { color: var(--brand-green); }
  .holder__title {
    display: inline-block;
    margin-top: 3px;
    padding: 1px 8px 1px 30px;
    background: var(--ink-white);
    color: var(--ink-black);
    font-size: 10px;
    letter-spacing: 0.5px;
    text-transform: uppercase;
  }

  .contact-band {
    position: absolute;
    left: 300px;
    right: 0;
    top: 186px;
    height: 66px;
    background: var(--brand-green);
    padding: 8px 12px;
    list-style: none;
    color: var(--ink-black);
    font-size: 12px;
    line-height: 1.35;
    text-transform: uppercase;
    white-space: nowrap;
  }
</style>
</head>
<body>
<main class="canvas">
  <section class="card card--back" aria-label="Card back">
    <div class="brand">
      <span class="brand__mark" aria-hidden="true"></span>
      <span class="brand__name">Dravetti Mining</span>
    </div>
  </section>

  <section class="card card--front" aria-label="Card front">
    <div class="front__haze" role="img" aria-label="Soft glow with translucent bokeh circles"></div>
    <div class="brand">
      <span class="brand__mark" aria-hidden="true"></span>
      <span class="brand__name">Dravetti Mining</span>
    </div>
    <div class="holder">
      <p class="holder__name"><span class="holder__name-initial">O</span>wen Pellsworth</p>
      <p class="holder__title">Managing Director</p>
    </div>
    <ul class="contact-band">
      <li>Owen@Dravetti-example.com</li>
      <li>972.555.0143</li>
      <li>3157 Brantley #5 Dallas, TX 75209</li>
    </ul>
  </section>
</main>
</body>
</html>
```